Tri-Fold Update

We need an old trifold brochure updated. We are going with a much cleaner and minimalistic design (see website velmorabrook.com). Want to update design to reflect more clean and modern feel. This will be a trifold brochure, see the attachments for the old version. Again, the content and concept of the old brochure needs to remain, but all design aspects can be updated.
We work in education, so if you want want to include artwork of schools, kids, etc feel free. If you want to have no art and have it white and clean, we would be open to that.
Logos for all 3 companies attached. Also attached is our new business card design so you can see the new "feel"
Target Market(s)
Senior executives
Industry/Entity Type
Business
Requirements
Must have
- all the logos and the content from the previous design. must be standard size for large trifold.

```html
<!DOCTYPE html>
<html lang="en">
<head>
<meta charset="utf-8">
<title>Tri-Fold Brochure – Inside Spread</title>
<link rel="stylesheet" href="https://fonts.googleapis.com/css2?family=Open+Sans:wght@400;600;700&display=swap">
<style>
  :root {
    --stage: #e2e3e5;
    --stage-edge: #c9cacc;
    --paper: #ffffff;
    --ink: #5a5d62;
    --ink-soft: #7a7d82;
    --academy-blue: #2f9fd8;
    --search-teal: #1fb7a1;
    --associates-pink: #d8567c;
    --tag-gold: #d6a52c;
    --tag-pink: #e2457c;
    --tag-teal: #22b49b;
    --tag-amber: #d39a2a;
    --logo-ink: #2b3f5c;
  }
  * { box-sizing: border-box; margin: 0; padding: 0; }
  html, body { width: 1200px; height: 800px; overflow: hidden; }
  body {
    font-family: "Open Sans", Arial, sans-serif;
    background: radial-gradient(ellipse at 50% 45%, var(--stage) 40%, var(--stage-edge) 100%);
    display: flex; align-items: center; justify-content: center;
  }
  .brochure {
    width: 1110px; height: 560px;
    display: flex;
    background: var(--paper);
    box-shadow: 0 18px 40px rgba(0,0,0,.22);
  }
  .panel {
    width: 370px; height: 100%;
    display: flex; flex-direction: column;
    position: relative;
  }
  .panel + .panel { border-left: 1px solid #ececec; }
  .panel-photo { height: 185px; width: 100%; }
  .photo-students { background: linear-gradient(160deg, #3f6b34 0%, #6f9a4a 45%, #c9b79b 75%, #7ea24c 100%); }
  .photo-search { background: linear-gradient(150deg, #efe3dc 0%, #d9bfb1 45%, #b7907d 75%, #e8d8cf 100%); }
  .photo-associates { background: linear-gradient(150deg, #f2f2f2 0%, #cfcfcf 40%, #5c5c5c 70%, #d8d8d8 100%); }

  .about-band {
    position: relative;
    height: 105px;
    padding: 12px 18px 0 128px;
    color: #fff;
  }
  .band-academy { background: var(--academy-blue); }
  .band-search { background: var(--search-teal); }
  .band-associates { background: var(--associates-pink); }
  .about-band h2 { font-size: 11.5px; font-weight: 600; margin-bottom: 5px; }
  .about-band p { font-size: 7.4px; line-height: 1.45; }
  .logo-tile {
    position: absolute; left: 18px; top: -26px;
    width: 96px; height: 96px;
    background: var(--paper);
    display: flex; align-items: center; justify-content: center;
    text-align: center;
    box-shadow: 0 2px 6px rgba(0,0,0,.12);
  }
  .logo-name {
    font-size: 12px; font-weight: 700; line-height: 1.2;
    color: var(--logo-ink);
  }

  .panel-body {
    flex: 1;
    display: grid; grid-template-columns: 1fr 1fr;
    column-gap: 14px;
    padding: 14px 16px 10px;
    align-content: start;
  }
  .column { display: flex; flex-direction: column; gap: 12px; }
  .service h3 {
    display: inline-flex; align-items: center; gap: 5px;
    font-size: 7.6px; font-weight: 700; color: #fff;
    padding: 2px 8px 2px 3px;
    margin-bottom: 5px;
  }
  .service h3 svg { width: 14px; height: 10px; flex: none; }
  .tag-gold { background: var(--tag-gold); }
  .tag-pink { background: var(--tag-pink); }
  .tag-teal { background: var(--tag-teal); }
  .tag-amber { background: var(--tag-amber); }
  .service p { font-size: 7.1px; line-height: 1.42; color: var(--ink); }
</style>
</head>
<body>
<svg width="0" height="0" style="position:absolute">
  <symbol id="book" viewBox="0 0 14 10">
    <rect x="0.5" y="0.5" width="13" height="9" fill="none" stroke="#fff" stroke-width="1"/>
    <path d="M7 2 V8.5 M2.5 2.5 H5.5 M2.5 4.5 H5.5 M8.5 2.5 H11.5 M8.5 4.5 H11.5" stroke="#fff" stroke-width="0.9"/>
  </symbol>
</svg>

<main class="brochure">
  <!-- Panel: academy -->
  <section class="panel">
    <div class="panel-photo photo-students" role="img" aria-label="Photo of a group of students sitting on the grass with books"></div>
    <div class="about-band band-academy">
      <div class="logo-tile"><span class="logo-name">The Lumen Academy</span></div>
      <h2>About The Lumen Academy</h2>
      <p>The Lumen Academy is a comprehensive not-for-profit leadership development program established nationally to prepare individuals for the next generation of superintendents and school district leaders. It prepares its fellows for the academic, political, legal and logistical complexities of the world that they seek to enter and lead.</p>
    </div>
    <div class="panel-body">
      <div class="column">
        <article class="service">
          <h3 class="tag-gold"><svg><use href="#book"/></svg>Lumen Academies</h3>
          <p>Lumen Academies are comprehensive leadership development experiences designed to prepare individuals for success in the superintendency. These programs benefit first-time superintendents, prospective superintendents, and members of a superintendent's executive team.</p>
        </article>
        <article class="service">
          <h3 class="tag-teal"><svg><use href="#book"/></svg>Alumni Services</h3>
          <p>Lumen continues to support cohort members after the Academy is completed by offering cohort members an online Academy network, maintaining professional contact with members of their cohort and giving notification of pertinent position postings and other announcements of interest. Staff will also provide resume advice and feedback to alumni seeking a superintendency.</p>
        </article>
      </div>
      <div class="column">
        <article class="service">
          <h3 class="tag-pink"><svg><use href="#book"/></svg>Superintendent Support Programs</h3>
          <p>It is important for new superintendents to quickly identify areas needing priority attention. Best practice reviews conducted during the first few months on the job can help uncover potential issue areas, provide an external expert viewpoint, and offer the research and support information necessary to make changes.</p>
        </article>
        <article class="service">
          <h3 class="tag-amber"><svg><use href="#book"/></svg>School Boardstreats &amp; Programs</h3>
          <p>An effective partnership between the superintendent and the board is critical to district success. Lumen provides cutting edge, customized governance team training and development, as well as facilitating board retreats.</p>
        </article>
      </div>
    </div>
  </section>

  <!-- Panel: search -->
  <section class="panel">
    <div class="panel-photo photo-search" role="img" aria-label="Sepia photo of a young woman reading at a desk beside a laptop"></div>
    <div class="about-band band-search">
      <div class="logo-tile"><span class="logo-name">Velmora Search</span></div>
      <h2>About Velmora Search</h2>
      <p>Velmora Search is a full service executive search firm with over 15 years of experience in helping schools and school districts find their new leaders. Velmora has the capacity, track record, and proven model to ensure that K12 school systems and charter organizations will be filled with the most effective and qualified leaders.</p>
    </div>
    <div class="panel-body">
      <div class="column">
        <article class="service">
          <h3 class="tag-gold"><svg><use href="#book"/></svg>Superintendent Searches</h3>
          <p>Velmora has refined our model, grown our team of search consultants, and increased our national network so that we are better prepared to assist school boards in a successful search for their district's next superintendent.</p>
        </article>
        <article class="service">
          <h3 class="tag-teal"><svg><use href="#book"/></svg>Teacher Searches</h3>
          <p>Velmora has invested in a new model driven by an innovative technology to assist school districts in recruiting, screening, vetting and predicting the most successful teachers. Our solution increases the quality of the teacher pool while reducing district overhead. We also fill the teacher vacancies quickly, with teachers more likely to succeed in the unique needs of the school and district.</p>
        </article>
      </div>
      <div class="column">
        <article class="service">
          <h3 class="tag-pink"><svg><use href="#book"/></svg>Administrator Searches</h3>
          <p>Velmora Search can quickly and efficiently fill critical administrative positions with the best fit leaders from across the country. We are the only company that has dedicated resources and processes to ensure your central office is filled with talent.</p>
        </article>
        <article class="service">
          <h3 class="tag-amber"><svg><use href="#book"/></svg>Principal Searches</h3>
          <p>Velmora has created a new and unique model to assist school districts in recruiting top quality principal candidates. By partnering with Velmora, districts can be assured that their schools will be filled with the best and brightest school reformers.</p>
        </article>
      </div>
    </div>
  </section>

  <!-- Panel: associates -->
  <section class="panel">
    <div class="panel-photo photo-associates" role="img" aria-label="Black and white photo of a young woman reading a book on a bench"></div>
    <div class="about-band band-associates">
      <div class="logo-tile"><span class="logo-name">Corvine Associates</span></div>
      <h2>About Corvine Associates</h2>
      <p>Corvine Associates helps K-12 institutions assess, determine, develop and implement reform strategies in order to improve student achievement at both the school and district level. Our holistic student approach to turnaround services provides nourishment and support for financial, operational, and educational initiatives.</p>
    </div>
    <div class="panel-body">
      <div class="column">
        <article class="service">
          <h3 class="tag-gold"><svg><use href="#book"/></svg>District Support Programs</h3>
          <p>Corvine offers district level support by assisting superintendents in making successful transitions. This support includes the development of a short-term plan, reviewing existing programs and creating organizational systems. Assisting superintendents and governance through a district-wide review that examines current initiatives, the organizational structure and implementation of the board's mission.</p>
        </article>
        <article class="service">
          <h3 class="tag-teal"><svg><use href="#book"/></svg>Scholastic Audit &amp; Quality Review</h3>
          <p>Corvine Associates' Quality Review process is a unique service that provides an accurate and concise glimpse into the state of affairs within the various levels of a district.</p>
        </article>
      </div>
      <div class="column">
        <article class="service">
          <h3 class="tag-pink"><svg><use href="#book"/></svg>Superintendent Support Programs</h3>
          <p>At the core of the Corvine support model is a strong focus on helping leaders to improve their instructional skills. A team of professionals with comparable experience will work directly with leaders. Our model is one with a primary emphasis on in-class assistance.</p>
        </article>
        <article class="service">
          <h3 class="tag-amber"><svg><use href="#book"/></svg>Principal Support Programs</h3>
          <p>Based on an audit and quality review, Corvine will design a customized program of support that will assist the principal throughout the school year to offer guidance, support, development and leadership assistance.</p>
        </article>
      </div>
    </div>
  </section>
</main>
</body>
</html>
```